Vexor Mind Social Media Advertisement

We need a social media advertisement made up for our Asset Insight. Our initial campaign will be on Reddit, so it needs to be compliant with reddit. Attached is a brief, we just need 1 single design initially that we can interchange the copy to see what converts better. Must be in a format that we can easily edit. Attached also are some examples of advertisements that are currently posted on Reddit for similar products. Coinsprig is the closest competitor. Please visit our website: https://www.vexormind.example to understand more about the business. You can also register as a free user to view the platform.

Target Market(s)

Self-directed Australian investors — particularly Self managed super fund trustees and property investors — who actively manage their own wealth and want AI-powered insights to make smarter financial decisions.

Industry/Entity Type

Financial technology (FinTech) / Wealth management software.

Requirements
Must have
• Dark, sophisticated colour palette (navy and teal), no emoji or decorative icons, clean and modern typography, and imagery that conveys intelligence, data, and financial confidence — not generic stock market clichés.
Nice to have
• Subtle futuristic or tech aesthetic, data visualisation elements (charts, graphs, network nodes), a sense of calm authority rather than aggressive "get rich" energy, and designs that would work across both digital ads and print formats.
Should not have
• Bright or garish colours, cartoonish illustrations, generic stock market imagery (bulls, bears, ticker tape), cluttered layouts, anything that feels salesy or hype-driven, and no cryptocurrency or "get rich quick" visual cues.

```html
<!DOCTYPE html>
<html lang="en">
<head>
<meta charset="utf-8">
<title>Vexor Mind – Asset Insight Ad</title>
<link rel="stylesheet" href="https://fonts.googleapis.com/css2?family=Ubuntu:wght@500;700&family=Poppins:wght@400;500&display=swap">
<style>
  :root{
    --navy-deep:#050a15;
    --navy:#0a1426;
    --navy-mid:#0d1c33;
    --teal:#2fd6c0;
    --teal-button:#16b39b;
    --cyan-glow:#1fb8e6;
    --white:#ffffff;
    --soft-white:#e9eef5;
  }
  html,body{margin:0;padding:0;width:1200px;height:1188px;overflow:hidden;background:var(--navy-deep);}
  .ad{
    position:relative;width:1200px;height:1188px;overflow:hidden;
    background:linear-gradient(180deg,var(--navy) 0%,var(--navy-deep) 100%);
    font-family:"Poppins",sans-serif;color:var(--white);
  }
  .ad__visual{
    position:absolute;inset:0;
    background:
      radial-gradient(ellipse 120px 90px at 1065px 480px, rgba(47,200,240,.45), transparent 70%),
      radial-gradient(ellipse 140px 100px at 795px 690px, rgba(47,200,240,.38), transparent 70%),
      radial-gradient(ellipse 110px 110px at 100px 525px, rgba(47,190,240,.25), transparent 70%),
      radial-gradient(ellipse 520px 180px at 560px 880px, rgba(20,120,170,.28), transparent 70%),
      radial-gradient(ellipse 420px 520px at 1020px 520px, rgba(20,110,160,.25), transparent 70%),
      radial-gradient(ellipse 300px 240px at 1000px 850px, rgba(15,90,130,.2), transparent 70%);
  }
  .ad__brand{
    position:absolute;top:52px;right:58px;
    display:flex;align-items:center;gap:12px;
    font-family:"Ubuntu",sans-serif;font-weight:500;font-size:40px;color:var(--white);
  }
  .ad__brand-dot{width:12px;height:12px;border-radius:50%;background:var(--teal);}
  .divider{
    position:absolute;left:99px;width:360px;height:2px;
    background:linear-gradient(90deg,transparent,var(--teal) 40%,transparent);
    opacity:.7;
  }
  .divider--top{top:149px;}
  .divider--bottom{top:517px;}
  .headline{
    position:absolute;left:71px;top:170px;margin:0;
    font-family:"Ubuntu",sans-serif;font-weight:700;line-height:1;
  }
  .headline__lead{display:block;font-size:73px;color:var(--white);}
  .headline__accent{display:block;font-size:93px;color:var(--teal);margin-top:12px;letter-spacing:-.5px;}
  .subline{
    position:absolute;left:75px;top:380px;margin:0;
    font-size:32px;line-height:54px;color:var(--soft-white);font-weight:400;
  }
  .baseline-glow{
    position:absolute;left:0;right:0;top:1006px;height:3px;
    background:linear-gradient(90deg,rgba(31,184,230,.9),rgba(31,184,230,.45) 40%,rgba(31,184,230,.8) 80%,rgba(31,184,230,.4));
    box-shadow:0 0 14px rgba(31,184,230,.7);
  }
  .tagline{
    position:absolute;left:73px;top:1042px;margin:0;
    display:flex;align-items:center;gap:20px;
    font-size:21px;font-weight:500;letter-spacing:10px;color:var(--soft-white);
  }
  .tagline__arrow{width:0;height:0;border-top:6px solid transparent;border-bottom:6px solid transparent;border-left:10px solid var(--teal);}
  .cta{
    position:absolute;left:772px;top:1022px;width:342px;height:65px;
    display:flex;align-items:center;justify-content:center;gap:14px;
    background:var(--teal-button);border-radius:5px;
    font-family:"Ubuntu",sans-serif;font-weight:500;font-size:27px;letter-spacing:-.5px;color:var(--white);
    text-decoration:none;
  }
</style>
</head>
<body>
<main class="ad">
  <div class="ad__visual" role="img" aria-label="Glowing cyan data waves and connected network nodes rising from lower left to upper right"></div>

  <div class="ad__brand"><span>Vexor Mind</span><span class="ad__brand-dot"></span></div>

  <div class="divider divider--top"></div>
  <h1 class="headline">
    <span class="headline__lead">Intelligence for</span>
    <span class="headline__accent">Serious investors.</span>
  </h1>
  <p class="subline">AI-powered insight for<br>Smarter wealth decisions</p>
  <div class="divider divider--bottom"></div>

  <div class="baseline-glow"></div>

  <p class="tagline">
    <span>CLARITY</span><span class="tagline__arrow"></span>
    <span>INSIGHT</span><span class="tagline__arrow"></span>
    <span>CONFIDENCE</span>
  </p>

  <a class="cta" href="#">Explore Vexor Mind
    <svg width="48" height="16" viewBox="0 0 48 16" aria-hidden="true"><path d="M0 8H45M38 2l7 6-7 6" fill="none" stroke="#fff" stroke-width="2"/></svg>
  </a>
</main>
</body>
</html>
```